Company or website name
- LORAVEX
- Links to the website
- WWW.LORAVEX.NET
- Describe your company and organization and target audience
- check the website: www.loravex.net
- The design should have the following
- A clean visual is expected. The documents should include the complete address, emails, phone, name and position.
- Other Facts

```html
<!DOCTYPE html>
<html lang="en">
<head>
<meta charset="utf-8">
<title>Loravex Business Card</title>
<link rel="stylesheet" href="https://fonts.googleapis.com/css2?family=Montserrat:wght@400;500&family=Open+Sans:wght@400;700&display=swap">
<style>
  :root {
    --navy: #0d3358;
    --navy-deep: #0a2a4a;
    --cyan: #5cc0d4;
    --paper: #f5f6f6;
    --ink: #2d3a46;
    --backdrop: #e9e7e4;
    --white: #ffffff;
  }
  * { box-sizing: border-box; margin: 0; padding: 0; }
  html, body {
    width: 1200px; height: 944px; overflow: hidden;
    background: var(--backdrop);
  }
  .canvas { position: relative; width: 1200px; height: 944px; }
  .card {
    position: absolute; width: 540px; height: 310px;
    box-shadow: 0 6px 18px rgba(0,0,0,0.12);
    overflow: hidden;
  }
  /* Front */
  .card-front { left: 90px; top: 140px; background: var(--navy); }
  .front-title {
    position: absolute; left: 0; right: 0; top: 128px; text-align: center;
    font-family: "Montserrat", sans-serif; font-weight: 500; font-size: 28px;
    letter-spacing: 0.5px; color: var(--white);
  }
  .front-title .tagline { color: var(--cyan); }
  .front-url {
    position: absolute; left: 0; right: 0; top: 240px; text-align: center;
    font-family: "Open Sans", sans-serif; font-size: 11px; letter-spacing: 3px;
    color: #c9d3dd;
  }
  /* Back */
  .card-back { left: 570px; top: 494px; background: var(--paper); }
  .brand {
    position: absolute; left: 40px; top: 88px;
    font-family: "Montserrat", sans-serif; font-weight: 400; font-size: 54px;
    letter-spacing: 2px; color: var(--navy);
  }
  .divider {
    position: absolute; left: 40px; top: 176px; width: 460px; height: 1px;
    background: var(--navy);
  }
  .person {
    position: absolute; right: 40px; top: 128px; text-align: right;
    font-family: "Open Sans", sans-serif;
  }
  .person-name { font-weight: 700; font-size: 19px; color: var(--navy); line-height: 1.2; }
  .person-role { font-size: 10px; color: var(--ink); margin-top: 6px; }
  .address {
    position: absolute; right: 40px; top: 206px; text-align: right;
    font-family: "Open Sans", sans-serif; font-size: 11.5px; line-height: 1.45; color: var(--ink);
  }
  .contacts {
    position: absolute; left: 40px; top: 196px; list-style: none;
    font-family: "Open Sans", sans-serif; font-size: 12px; color: var(--ink);
  }
  .contacts li { display: flex; align-items: center; gap: 7px; height: 18px; }
  .contacts svg { width: 11px; height: 11px; fill: var(--navy); }
  .band { position: absolute; left: 0; top: 0; width: 540px; height: 310px; }
  .band-url {
    position: absolute; right: 40px; top: 266px;
    font-family: "Open Sans", sans-serif; font-size: 11px; letter-spacing: 3px; color: var(--white);
  }
</style>
</head>
<body>
<main class="canvas">
  <section class="card card-front" aria-label="Card front">
    <h1 class="front-title">LORAVEX <span class="tagline">DRILLING SUPPLIES</span></h1>
    <p class="front-url">www.loravex.net</p>
  </section>

  <section class="card card-back" aria-label="Card back">
    <svg class="band" viewBox="0 0 540 310" aria-hidden="true">
      <polyline points="0,283 326,283 346,255 540,255" fill="none" stroke="var(--cyan)" stroke-width="2"/>
      <polygon points="0,290 330,290 350,262 540,262 540,310 0,310" fill="var(--navy)"/>
    </svg>
    <div class="brand">LORAVEX</div>
    <div class="divider"></div>
    <div class="person">
      <div class="person-name">Dale Morrowfield</div>
      <div class="person-role">President</div>
    </div>
    <address class="address" style="font-style:normal">
      Villa Serena, Altos del Prado<br>Ciudad de Panama
    </address>
    <ul class="contacts">
      <li><svg viewBox="0 0 12 12"><path d="M2.5 1l2 2-1 1.5c.7 1.6 1.9 2.8 3.5 3.5L8.5 7l2 2-1.5 2C5 10.5 1.5 7 1 2.5z"/></svg>+507 814-2270</li>
      <li><svg viewBox="0 0 12 12"><path d="M3 0h6v12H3zM4 1.5v8h4v-8z"/></svg>+507 6358-4417</li>
      <li><svg viewBox="0 0 12 12"><path d="M0 2h12v8H0zM1 3l5 3.5L11 3z" fill-rule="evenodd"/></svg>sales@loravex.net</li>
    </ul>
    <p class="band-url">www.loravex.net</p>
  </section>
</main>
</body>
</html>
```